Building company requiring web site design

We need a web design for a new company based in Sydney called Marlow Building Co. We build and renovate new and existing homes for consumers. We would like to see design that use the colours red and grey. The final design should communicate innovative building but with old fashion quality, great customer service and attention to detail. I have already had a logo and stationary design completed and would like to use the these colour schemes
Updates

Target Market(s)

Home owners, investors

Industry/Entity Type

Building

Coding

Coded - Design and coding required

Number of Pages Required

5+ page

Requirements
Must have
• Home page, contact page, about us page, gallery page and testimonial page
Nice to have
• Contact form

```html
<!DOCTYPE html>
<html lang="en">
<head>
<meta charset="utf-8">
<title>Marlow Building Co. — Home</title>
<link rel="stylesheet" href="https://fonts.googleapis.com/css2?family=Open+Sans:wght@400;600;700&family=Ubuntu:wght@400;500;700&display=swap">
<style>
:root{
  --red:#b5474b;
  --red-dark:#9e3a3e;
  --ink:#333333;
  --text:#555555;
  --muted:#8a8a8a;
  --line:#bdbdbd;
  --topbar:#2b2b2b;
  --footer:#262626;
  --footer-base:#1c1c1c;
  --panel:#e8e8e8;
  --white:#ffffff;
}
*{box-sizing:border-box;margin:0;padding:0}
html,body{width:1200px;height:2647px;overflow:hidden}
body{position:relative;background:var(--white);font-family:"Open Sans",Arial,sans-serif;color:var(--text)}
.abs{position:absolute}

/* top bar */
.topbar{left:0;top:0;width:1200px;height:25px;background:var(--topbar);color:#b0b0b0;font-size:11px}
.topbar .item{position:absolute;top:5px;display:flex;align-items:center;gap:6px}
.topbar svg{width:10px;height:10px;fill:#b0b0b0}

/* header */
.header{left:0;top:25px;width:1200px;height:113px;background:var(--white)}
.brand{position:absolute;left:99px;top:46px;display:flex;align-items:center;gap:12px;font-family:"Ubuntu",sans-serif;font-weight:700;color:var(--ink);font-size:22px;line-height:1.1}
.brand .mark{width:30px;height:30px;background:var(--red)}
.nav{position:absolute;top:47px;left:0;width:1200px;font-family:"Ubuntu",sans-serif;font-size:13px;color:var(--ink)}
.nav a{position:absolute;color:inherit;text-decoration:none;white-space:nowrap}
.nav a.active::after{content:"";position:absolute;left:0;right:0;top:25px;height:3px;background:var(--red)}

/* hero */
.hero{left:0;top:138px;width:1200px;height:483px;background:linear-gradient(180deg,#5e5a55 0%,#3d3a37 55%,#2a2826 100%)}
.hero-frame{left:312px;top:258px;width:574px;height:238px;border:1.5px solid var(--red);text-align:center;color:#fff}
.hero-frame h1{font-family:"Ubuntu",sans-serif;font-weight:500;font-size:35px;margin-top:56px}
.hero-frame p{font-size:12.5px;line-height:18px;width:530px;margin:12px auto 0}
.dots{left:590px;top:594px;display:flex;gap:4px}
.dots span{width:8px;height:8px;border-radius:50%;border:1px solid #ccc}
.dots span.on{background:#ccc}

/* section titles */
.title{left:0;width:1200px;height:40px}
.title .rule{position:absolute;top:16px;height:1px;background:var(--line)}
.title .box{position:absolute;left:50%;transform:translateX(-50%);top:0;height:40px;border-left:1px solid var(--line);border-right:1px solid var(--line);padding:0 22px;text-align:center}
.title h2{font-family:"Ubuntu",sans-serif;font-weight:500;font-size:18px;color:var(--ink);line-height:22px;margin-top:-3px}
.title small{display:block;font-size:11.5px;color:var(--muted);line-height:16px}

.about-copy{left:185px;top:733px;width:820px;font-size:12.4px;line-height:18.5px;color:var(--text)}

/* red bands */
.band{left:0;width:1200px;background:var(--red);color:#fff}
.band .headline{position:absolute;left:184px;font-family:"Ubuntu",sans-serif;font-weight:700;font-size:24px;white-space:nowrap}
.band .headline span{font-size:17px}
.btn-outline{position:absolute;border:2px solid #fff;border-radius:3px;color:#fff;font-family:"Ubuntu",sans-serif;font-weight:500;font-size:17px;display:flex;align-items:center;justify-content:center}

.illustration{left:0;top:921px;width:1200px;height:212px;background:linear-gradient(180deg,#f6efc9 0%,#d8e6e8 60%,#c9dbe3 100%)}

/* services */
.services{left:0;top:1133px;width:1200px;height:388px;background:var(--panel)}
.service{position:absolute;top:1292px;width:330px;text-align:center}
.service .icon{width:86px;height:86px;margin:0 auto;border:2px solid var(--red);border-radius:4px;display:flex;align-items:center;justify-content:center}
.service .icon svg{width:56px;height:56px}
.service.featured .icon{background:var(--red)}
.service h3{margin-top:26px;font-size:13px;font-weight:700;color:#555}
.service.featured h3{color:var(--red)}
.service p{margin-top:18px;font-size:12.3px;line-height:17.5px;color:#666}

/* gallery */
.thumb{position:absolute;width:231px;height:184px;border-radius:4px}
.thumb.hover{background:#7d3a2f}
.thumb.hover .inner{position:absolute;left:24px;top:24px;right:24px;bottom:24px;border:1px solid rgba(255,255,255,.35);background:rgba(181,71,75,.55);display:flex;align-items:center;justify-content:center;gap:12px}
.thumb.hover .inner span{width:30px;height:30px;border:1.5px solid #fff;display:flex;align-items:center;justify-content:center}
.btn-red{left:526px;top:2157px;width:148px;height:42px;border:2px solid var(--red);border-radius:4px;color:var(--red);font-family:"Ubuntu",sans-serif;font-weight:500;font-size:17px;display:flex;align-items:center;justify-content:center}

/* testimonial */
.testimonial{left:0;top:2224px;width:1200px;height:158px;background:var(--red);color:#fff}
.avatar{left:226px;top:2252px;width:86px;height:101px;border:2px solid #ddd;background:linear-gradient(160deg,#9a8c80,#5f554e)}
.quote{left:339px;top:2261px;width:640px;font-size:13px;line-height:17.5px}
.quote cite{display:block;margin-top:12px;margin-left:6px;font-style:normal;font-weight:700;font-size:12px}

/* footer */
.footer{left:0;top:2382px;width:1200px;height:239px;background:var(--footer)}
.footer h4{position:absolute;top:2424px;font-family:"Ubuntu",sans-serif;font-weight:500;font-size:16px;color:var(--red)}
.email{left:99px;top:2464px;width:224px;height:28px;background:#3b3b3b;color:#aaa;font-size:11.5px;display:flex;align-items:center;gap:8px;padding-left:8px}
.email svg{width:22px;height:16px}
.submit{left:330px;top:2464px;width:86px;height:28px;border:1.5px solid var(--red);color:#fff;font-size:12px;font-weight:700;display:flex;align-items:center;justify-content:center}
.social{position:absolute;top:2541px;width:28px;height:28px;background:#6d6d6d;border-radius:2px}
.posts{left:528px;top:2459px;width:290px;font-size:11.5px;color:#9a9a9a;line-height:16px}
.posts p{padding-bottom:8px;margin-bottom:10px;border-bottom:1px solid #4a4a4a}
.links{top:2459px;font-size:11.5px;color:#9a9a9a;line-height:18px}
.copyright{left:0;top:2621px;width:1200px;height:26px;background:var(--footer-base);color:#8a8a8a;font-size:11px;text-align:center;line-height:26px}
</style>
</head>
<body>

<div class="abs topbar">
  <div class="item" style="left:878px">
    <svg viewBox="0 0 10 10"><path d="M2 0.5 L3.6 2.6 L2.8 3.6 Q4 6 6.4 7.2 L7.4 6.4 L9.5 8 L8.3 9.5 Q1 8 0.5 1.7 Z"/></svg>
    24x7 Customer Service
  </div>
  <div class="item" style="left:1052px">
    <svg viewBox="0 0 10 10"><rect x="1.5" y="4.5" width="7" height="5.5"/><path d="M3 4.5 V3 a2 2 0 0 1 4 0 V4.5" fill="none" stroke="#b0b0b0" stroke-width="1.2"/></svg>
    Log In
  </div>
</div>

<header class="abs header">
  <div class="brand"><span class="mark"></span><span>Marlow<br>Building Co.</span></div>
</header>
<nav class="nav" style="position:absolute;top:72px">
  <a class="active" style="left:702px">HOME</a>
  <a style="left:770px">ABOUT</a>
  <a style="left:843px">GALLERY</a>
  <a style="left:928px">TESTIMONIAL</a>
  <a style="left:1031px">CONTACT US</a>
</nav>

<section class="abs hero" role="img" aria-label="Photo of builders working inside a house under construction"></section>
<div class="abs hero-frame">
  <h1>Your Dream house</h1>
  <p>Lorem ipsum dolor sit amet, consectetuer adipiscing elit, sed diam nonummy nibh dolore magna aliquam erat volutpat. Ut wisi enim ad minim veniam, quis praesent dele nit augue duis dolore te feugait nulla facilisi.</p>
</div>
<div class="abs dots"><span class="on"></span><span></span></div>

<div class="abs title" style="top:665px">
  <div class="rule" style="left:356px;width:172px"></div>
  <div class="rule" style="left:674px;width:172px"></div>
  <div class="box"><h2>ABOUT US</h2><small>and our Priorities</small></div>
</div>
<p class="abs about-copy">Lorem ipsum dolor sit amet, consectetuer adipiscing elit, sed diam nonummy nibh euismod tincidunt ut laoreet dolore magna aliquam erat volutpat. Ut wisi enim ad minim veniam, quis nostrud exerci tation ullamcorper suscipit lobortis nisl ut aliquip ex ea commodo consequat. Duis autem vel eum iriure dolor in hendrerit in vulputate velit esse molestie consequat, vel illum dolore eu feugiat nulla facilisis at vero eros et accumsan et iusto odio dignissim qui blandit praesent luptatum zzril delenit augue duis dolore te feugait nulla facilisi.</p>

<section class="abs band" style="top:833px;height:88px">
  <div class="headline" style="top:27px">CONSTRUCTION FIRM SENCE 1900, <span>WE BUILD YOUR DREAMS</span></div>
  <div class="btn-outline" style="left:870px;top:23px;width:148px;height:41px">Get a Quote</div>
</section>

<div class="abs illustration" role="img" aria-label="Illustration of a smiling builder in a hard hat pointing down, in front of a city skyline"></div>

<section class="abs services"></section>
<div class="abs title" style="top:1208px">
  <div class="rule" style="left:337px;width:172px"></div>
  <div class="rule" style="left:690px;width:172px"></div>
  <div class="box"><h2>OUR SERVICE</h2><small>Lorem ipsum is dummy</small></div>
</div>

<div class="service" style="left:86px">
  <div class="icon"><svg viewBox="0 0 56 56" fill="none" stroke="#555" stroke-width="2.5"><rect x="12" y="22" width="24" height="26"/><path d="M36 30 H46 V48 H36 M30 22 V8 M22 12 H44 M40 12 V18"/><path d="M17 28h4M25 28h4M17 35h4M25 35h4M17 42h4M25 42h4"/></svg></div>
  <h3>SERVICE 1</h3>
  <p>ipsum dolor sit amet, consectetuer adipiscing elit, sed diam nonummy nibh euismod tincidunt ut laoreet dolore magna aliquam erat volutpat.</p>
</div>
<div class="service featured" style="left:435px">
  <div class="icon"><svg viewBox="0 0 56 56" fill="none" stroke="#fff" stroke-width="3"><circle cx="28" cy="28" r="14"/><circle cx="28" cy="28" r="6"/><path d="M28 6v8M28 42v8M6 28h8M42 28h8M12.5 12.5l5.5 5.5M38 38l5.5 5.5M12.5 43.5l5.5-5.5M38 18l5.5-5.5"/></svg></div>
  <h3>SERVICE 2</h3>
  <p>Lorem ipsum dolor sit amet, consectetuer adipiscing elit, sed diam nonummy nibh euismod tincidunt ut laoreet dolore magna aliquam erat volutpat.</p>
</div>
<div class="service" style="left:784px">
  <div class="icon"><svg viewBox="0 0 56 56" fill="none" stroke="#555" stroke-width="2.5"><path d="M6 26 L28 8 L50 26 M12 22 V48 H44 V22"/><path d="M22 48 V34 H34 V48 M20 26 H36"/></svg></div>
  <h3>SERVICE 3</h3>
  <p>ipsum dolor sit amet, consectetuer adipiscing elit, sed diam nonummy nibh euismod tincidunt ut laoreet dolore magna aliquam erat volutpat.</p>
</div>

<section class="abs band" style="top:1521px;height:87px">
  <div class="headline" style="top:26px">GET YOUR FREE CONSULTANT</div>
  <div class="btn-outline" style="left:868px;top:23px;width:148px;height:41px">Contact us</div>
</section>

<div class="abs title" style="top:1649px">
  <div class="rule" style="left:337px;width:172px"></div>
  <div class="rule" style="left:690px;width:172px"></div>
  <div class="box"><h2>Our Gallery</h2><small>Lorem ipsum is dummy</small></div>
</div>

<div class="thumb" style="left:99px;top:1724px;background:linear-gradient(160deg,#9fbf7a,#d9d6cf)" role="img" aria-label="Photo of a bright living room opening onto a garden"></div>
<div class="thumb" style="left:355px;top:1724px;background:linear-gradient(180deg,#a89a7c,#cfc7b5 60%,#4fb7c4)" role="img" aria-label="Photo of a thatched villa with a pool"></div>
<div class="thumb" style="left:614px;top:1724px;background:linear-gradient(180deg,#e2b45c,#b98456 55%,#3d7f96)" role="img" aria-label="Photo of canal houses and boats"></div>
<div class="thumb" style="left:870px;top:1724px;background:linear-gradient(180deg,#7fa8c4,#6f7d5b 55%,#8f6a44)" role="img" aria-label="Photo of a terrace with wooden furniture by a lake"></div>
<div class="thumb" style="left:99px;top:1936px;background:linear-gradient(160deg,#e7dcc4,#b9a885)" role="img" aria-label="Photo of a living room with a fireplace and chandelier"></div>
<div class="thumb" style="left:355px;top:1936px;background:linear-gradient(160deg,#ece4d2,#c9b79a)" role="img" aria-label="Photo of a lounge with framed pictures and plants"></div>
<div class="thumb hover" style="left:614px;top:1936px" role="img" aria-label="Gallery photo with zoom and link controls">
  <div class="inner">
    <span><svg width="18" height="18" viewBox="0 0 18 18" fill="none" stroke="#fff" stroke-width="2"><circle cx="7.5" cy="7.5" r="5"/><path d="M11 11l5 5"/></svg></span>
    <span><svg width="18" height="18" viewBox="0 0 18 18" fill="none" stroke="#fff" stroke-width="2"><path d="M8 10l2-2M6.5 8.5l-2.5 2.5a2.1 2.1 0 0 0 3 3l2.5-2.5M11.5 9.5l2.5-2.5a2.1 2.1 0 0 0-3-3L8.5 6.5"/></svg></span>
  </div>
</div>
<div class="thumb" style="left:870px;top:1936px;background:linear-gradient(160deg,#c8d6e0,#e9e6e0 60%,#8a7560)" role="img" aria-label="Photo of a modern sunlit living room"></div>

<div class="abs btn-red">View All</div>

<section class="abs testimonial"></section>
<div class="abs avatar" role="img" aria-label="Portrait of the client giving the testimonial"></div>
<blockquote class="abs quote">“Lorem ipsum dolor sit amet, consectetuer adipiscing elit, sed diam nonummy nibh euismod tincidunt tation ullamcorper suscipit lobortis nisl ut aliquip ex ea feugiat nulla facilisis at vero eros et accumsan et iusto odio dignissim qui blandit praesent luptatum zzril delenit augue duis dolore”
  <cite>- Tam Rivers</cite>
</blockquote>

<footer class="abs footer"></footer>
<h4 style="left:99px">Stay Connected</h4>
<h4 style="left:528px">Latest Posts</h4>
<h4 style="left:870px">Quick Links</h4>

<div class="abs email">
  <svg viewBox="0 0 22 16" fill="none" stroke="#ccc" stroke-width="1.4"><rect x="1" y="1" width="20" height="14"/><path d="M1 1l10 8 10-8"/></svg>
  Enter your Email
</div>
<div class="abs submit">Submit</div>
<span class="social" style="left:99px" aria-label="Social link"></span>
<span class="social" style="left:139px" aria-label="Social link"></span>
<span class="social" style="left:178px" aria-label="Social link"></span>
<span class="social" style="left:217px" aria-label="Social link"></span>

<div class="abs posts">
  <p>“Neque porro quisquam est qui dolorem ipsum quia dolor sit amet, consectetur, adipisci velit...”</p>
  <p>“Neque porro quisquam est qui dolorem ipsum quia dolor sit amet, consectetur, adipisci velit...”</p>
  <p>“Neque porro quisquam est qui dolorem ipsum quia dolor sit amet, consectetur, adipisci velit...”</p>
</div>
<div class="abs links" style="left:870px">Our Story<br>Our Blog<br>Contact Us<br>Privacy Policy</div>
<div class="abs links" style="left:1001px;text-align:center">Our team<br>FAQ<br>Tearms &amp; Condition</div>

<div class="abs copyright">copyright 2016,</div>

</body>
</html>
```